Mark & Lisa's Hammock Season Party

Invitation to a party 60-80 people at a private residence. Age range 30-40s.

Themes: summer/casual/Australian backyard/local community

**For delivery via both email and printed copy**
Would like one document suitable for both purposes or two versions for electronic or paper invitation. I will arrange printing so please prepare it in a suitable format.

Specimen text attached. Address and phone contact to follow by message with successful bidder

Thanks!
Mark

Target Market(s)

Locals, friends. Party attendees will typicaly be parents in their forties who who be leaving the kids at home for a relaxed party night, and walking home afterward

Industry/Entity Type

Community

Font styles to use
Sans Serif

Requirements
Should not have
• Cliche Australiana imagery. No kangaroos etc

```html
<!DOCTYPE html>
<html lang="en">
<head>
<meta charset="utf-8">
<title>Mark &amp; Lisa's Hammock Season Party – Invitation</title>
<link rel="stylesheet" href="https://fonts.googleapis.com/css2?family=Saira+Condensed:wght@400;500;600&family=Playfair+Display:wght@400&family=Roboto:wght@400&display=swap">
<style>
  :root {
    --page-bg: #ffffff;
    --frame: #9a9a9a;
    --ink-light: #ffffff;
    --pink: #e46aa0;
    --magenta: #b63a8f;
    --violet: #6a3fc4;
    --royal: #3a2fbf;
    --navy: #16208a;
    --sky: #4fb3ea;
    --plum: #5a1c4a;
    --berry: #9c1f3e;
    --amber: #d89a45;
    --people-warm: #d9b39a;
    --people-cool: #e9eef3;
    --table-warm: #8a6a4e;
    --table-light: #d8c9a8;
    --display: "Saira Condensed", "Arial Narrow", sans-serif;
    --ampersand: "Playfair Display", Georgia, serif;
    --body: "Roboto", Arial, sans-serif;
  }
  * { margin: 0; padding: 0; box-sizing: border-box; }
  html, body {
    width: 1200px; height: 848px; overflow: hidden;
    background: var(--page-bg);
  }
  .canvas { position: relative; width: 1200px; height: 848px; }

  .page {
    position: absolute; top: 0; width: 592px; height: 848px;
    border: 1px solid var(--frame); overflow: hidden;
  }
  .page--front { left: 0; }
  .page--back { left: 606px; }

  /* Front page */
  .front-backdrop {
    position: absolute; inset: 0;
    background:
      linear-gradient(180deg, rgba(255,255,255,0) 40%, #fff 62%),
      linear-gradient(90deg, var(--pink) 0%, var(--violet) 18%, var(--violet) 70%, var(--royal) 82%, var(--sky) 100%);
  }
  .people-photo {
    position: absolute; left: 36px; top: 516px; width: 528px; height: 332px;
    background: radial-gradient(ellipse at 50% 55%, var(--people-warm) 0%, #c7a7c6 45%, var(--people-cool) 80%, rgba(255,255,255,0) 100%);
  }
  .headline-arch {
    position: absolute; left: 115px; top: 0; width: 363px; height: 546px;
    border-radius: 0 0 182px 182px;
    background:
      radial-gradient(circle at 28% 16%, rgba(216,154,69,.55) 0 9%, transparent 20%),
      radial-gradient(circle at 62% 22%, rgba(216,154,69,.45) 0 8%, transparent 18%),
      radial-gradient(circle at 86% 40%, rgba(200,30,60,.8) 0 14%, transparent 22%),
      linear-gradient(180deg, #6b3a2a 0%, var(--berry) 35%, var(--plum) 70%, #3b1a5c 100%);
  }
  .headline {
    position: absolute; left: 115px; top: 0; width: 363px;
    text-align: center; color: var(--ink-light);
  }
  .headline__line {
    font-family: var(--display); font-weight: 500; text-transform: uppercase;
    font-size: 38px; line-height: 1; letter-spacing: .5px;
  }
  .headline__line--first { margin-top: 96px; }
  .headline__amp {
    font-family: var(--ampersand); font-size: 84px; line-height: 1;
    margin: 4px 0 2px;
  }
  .headline__at {
    font-family: var(--display); font-size: 28px; line-height: 1; margin-top: 6px;
  }
  .headline__hosts {
    font-family: var(--display); font-weight: 500; text-transform: uppercase;
    font-size: 19px; line-height: 1; margin-top: 10px;
  }
  .headline__event {
    font-family: var(--display); font-weight: 600; text-transform: uppercase;
    font-size: 27px; line-height: 1; margin-top: 4px;
  }
  .headline__guests {
    font-family: var(--display); font-weight: 500; text-transform: uppercase;
    font-size: 12px; line-height: 1; margin-top: 4px;
  }
  .details {
    font-family: var(--body); font-size: 14.5px; line-height: 21px; margin-top: 28px;
  }

  /* Back page */
  .back-backdrop {
    position: absolute; inset: 0;
    background:
      radial-gradient(circle at 6% 8%, rgba(255,160,170,.8) 0 10%, transparent 22%),
      radial-gradient(circle at 52% 6%, rgba(255,255,255,.25) 0 4%, transparent 8%),
      radial-gradient(circle at 100% 80%, rgba(79,179,234,.7) 0 10%, transparent 35%),
      linear-gradient(180deg, var(--magenta) 0%, var(--violet) 14%, var(--royal) 40%, var(--navy) 100%);
  }
  .dinner-photo {
    position: absolute; left: 0; top: 172px; width: 592px; height: 254px;
    background:
      radial-gradient(ellipse at 52% 75%, var(--table-light) 0 18%, transparent 40%),
      linear-gradient(90deg, #5b4636 0%, var(--table-warm) 35%, #c9a46a 60%, var(--table-warm) 85%, #4f3b2e 100%);
  }
  .notes {
    position: absolute; left: 0; top: 456px; width: 592px;
    text-align: center; color: var(--ink-light);
  }
  .notes__title {
    font-family: var(--display); font-weight: 600; text-transform: uppercase;
    font-size: 40px; line-height: 1; letter-spacing: .5px;
  }
  .notes__list, .notes__invite {
    font-family: var(--display); font-weight: 500; font-size: 21px; line-height: 24px;
  }
  .notes__list { margin-top: 4px; }
  .notes__invite { margin-top: 24px; }
  .rsvp {
    font-family: var(--body); font-size: 18.5px; line-height: 24px; margin-top: 43px;
  }
</style>
</head>
<body>
<main class="canvas">

  <section class="page page--front">
    <div class="front-backdrop"></div>
    <div class="people-photo" role="img" aria-label="Photo of a cheerful group of friends in summer dresses and party hats holding wrapped gifts"></div>
    <div class="headline-arch" role="img" aria-label="Warm bokeh party lights with a hanging red bauble and tinsel"></div>
    <header class="headline">
      <p class="headline__line headline__line--first">Leave the kids at home</p>
      <p class="headline__amp">&amp;</p>
      <p class="headline__line">Let your hair down</p>
      <p class="headline__at">at</p>
      <p class="headline__hosts">Mark &amp; Lisa's</p>
      <p class="headline__event">Hammock Season Party</p>
      <p class="headline__guests">For Fernleigh Heights and friends</p>
      <div class="details">
        <p>Saturday 2 January</p>
        <p>From 6pm ’til late</p>
        <p>25 Wattlebird Street, Fernleigh Heights</p>
      </div>
    </header>
  </section>

  <section class="page page--back">
    <div class="back-backdrop"></div>
    <div class="dinner-photo" role="img" aria-label="Photo of friends raising wine glasses over shared plates at an outdoor table"></div>
    <div class="notes">
      <h2 class="notes__title">Child-free event</h2>
      <div class="notes__list">
        <p>Dress: summer casual, bare feet welcome</p>
        <p>Cocktail food provided</p>
        <p>BYO but only if you insist</p>
      </div>
      <div class="notes__invite">
        <p>If you have some friends or neighbours that you like</p>
        <p>to hang out with,</p>
        <p>we would love to meet.</p>
        <p>Bring them with you!</p>
      </div>
      <div class="rsvp">
        <p>An RSVP for catering would be nice.</p>
        <p>Text Mark xxx xxxxxx or Lisa yyyyyyyy before Xmas please.</p>
      </div>
    </div>
  </section>

</main>
</body>
</html>
```